Flyer design for webdesign company

create a flyer that can be printed or sent as an email. The flyer needs to be professional, modern and engaging.

Reason: opportunity for all designers to get their designs in.

Target Market(s)

business owners that do not have a website

Industry/Entity Type

It Company

Font styles to use
Sans Serif

```html
<!DOCTYPE html>
<html lang="en">
<head>
<meta charset="utf-8">
<title>novawebworks flyer</title>
<link rel="stylesheet" href="https://fonts.googleapis.com/css2?family=Oswald:wght@500;700&family=Source+Sans+3:wght@400;600;700&display=swap">
<style>
  :root {
    --orange: #f7941d;
    --orange-dark: #e27d0c;
    --gray: #6d6e71;
    --blue: #1f5aa8;
    --blue-deep: #0d4f9e;
    --blue-bright: #1a73c8;
    --ink: #111;
    --text: #2b2b2b;
    --white: #fff;
  }
  * { margin: 0; padding: 0; box-sizing: border-box; }
  html, body { width: 953px; height: 1200px; overflow: hidden; }
  body { font-family: "Source Sans 3", sans-serif; color: var(--text); }
  .flyer {
    position: relative; width: 953px; height: 1200px; overflow: hidden;
    background: radial-gradient(ellipse at 40% 85%, #d9dadc 0%, #f4f4f5 45%, #fff 75%);
  }
  .backdrop { position: absolute; inset: 0; }

  .brand { position: absolute; left: 51px; top: 70px; width: 300px; height: 240px; }
  .brand-dot {
    position: absolute; left: 108px; top: 52px; width: 76px; height: 76px;
    border-radius: 50%; background: var(--orange);
  }
  .brand-name {
    position: absolute; left: 0; top: 196px; width: 300px;
    font-size: 44px; font-weight: 600; color: var(--orange); letter-spacing: 0.5px;
  }

  .badge {
    position: absolute; left: 664px; top: 42px; width: 210px; height: 210px;
    border-radius: 50%; background: var(--white);
    box-shadow: 0 6px 14px rgba(0,0,0,.25);
  }
  .badge-inner {
    position: absolute; inset: 16px; border-radius: 50%;
    background: radial-gradient(circle at 40% 30%, var(--blue-bright), var(--blue-deep) 70%);
    display: flex; align-items: center; justify-content: center;
  }
  .badge-text {
    transform: rotate(-15deg); text-align: center; color: var(--white);
    font-family: "Oswald", sans-serif; font-weight: 700; font-size: 38px; line-height: 1.05;
  }

  .call { position: absolute; right: 56px; top: 262px; text-align: right; }
  .call-label { font-size: 38px; font-weight: 400; letter-spacing: 1px; color: #222; line-height: 1; }
  .call-phone { font-family: "Oswald", sans-serif; font-weight: 700; font-size: 42px; color: var(--ink); line-height: 1.2; margin-top: 4px; }

  .headline {
    position: absolute; left: 49px; top: 360px;
    font-family: "Oswald", sans-serif; font-weight: 700; font-size: 41px;
    color: var(--orange); line-height: 53px; letter-spacing: 0.3px;
  }

  .benefits { position: absolute; left: 52px; top: 486px; list-style: none; }
  .benefits li {
    display: flex; align-items: center; height: 36px;
    font-size: 19px; color: var(--text);
  }
  .benefits svg { width: 20px; height: 18px; margin-right: 8px; flex: none; }

  .photo { position: absolute; left: 620px; width: 281px; height: 180px; }
  .photo-touchscreen { top: 385px; background: linear-gradient(135deg, #c9dced 0%, #7fa5c9 45%, #2a4a78 100%); }
  .photo-boardroom { top: 575px; background: linear-gradient(135deg, #3a4350 0%, #5d87b0 45%, #c8d0d8 100%); }

  .url-pill {
    position: absolute; left: 40px; top: 774px; width: 487px; height: 53px;
    border-radius: 18px 26px 26px 18px;
    background: linear-gradient(180deg, var(--blue-bright), var(--blue-deep));
    color: var(--white); font-weight: 700; font-size: 31px; letter-spacing: 0.6px;
    display: flex; align-items: center; padding-left: 26px;
  }

  .pitch {
    position: absolute; left: 49px; top: 851px;
    font-size: 45px; font-weight: 600; color: var(--blue); line-height: 56px;
  }

  .globe {
    position: absolute; left: 390px; top: 952px; width: 200px; height: 210px;
    border-radius: 50%;
    background: radial-gradient(circle at 40% 35%, #8ec3f0, #2467b5 60%, #0d3f7e 100%);
  }

  .price {
    position: absolute; left: 550px; top: 810px; width: 356px; height: 356px;
    border-radius: 50%; background: var(--orange);
    box-shadow: 0 6px 14px rgba(0,0,0,.25);
  }
  .price-inner {
    position: absolute; inset: 20px; border-radius: 50%;
    background: radial-gradient(circle at 50% 40%, #fff 60%, #e4e4e6 100%);
    text-align: center; padding-top: 36px;
  }
  .price-label { font-family: "Oswald", sans-serif; font-weight: 500; font-size: 40px; color: var(--ink); line-height: 1.1; }
  .price-amount { font-family: "Oswald", sans-serif; font-weight: 700; font-size: 52px; color: var(--orange); line-height: 54px; margin-top: 2px; }
  .price-note { font-size: 25px; color: #111; line-height: 1.25; margin-top: 8px; }

  .footer-phone {
    position: absolute; left: 43px; top: 1116px;
    font-family: "Oswald", sans-serif; font-weight: 700; font-size: 50px; color: var(--ink); line-height: 1.2;
  }
</style>
</head>
<body>
<main class="flyer">
  <svg class="backdrop" width="953" height="1200" viewBox="0 0 953 1200" aria-hidden="true">
    <path d="M0,0 H953 V200 Q560,-20 0,16 Z" fill="var(--orange)"/>
    <path d="M0,16 Q560,-20 953,200 V258 Q560,10 0,30 Z" fill="var(--gray)"/>
    <path d="M0,1026 Q420,1120 953,1125 V1200 H0 Z" fill="var(--orange)"/>
    <path d="M240,1085 Q600,1100 953,1100 V1112 Q600,1115 240,1085 Z" fill="var(--blue-deep)"/>
  </svg>

  <div class="brand">
    <span class="brand-dot"></span>
    <span class="brand-name">novawebworks</span>
  </div>

  <div class="badge"><div class="badge-inner"><div class="badge-text">ONLY<br>$3<br>A DAY</div></div></div>

  <div class="call">
    <div class="call-label">CALL TODAY</div>
    <div class="call-phone">1-800-555-0142</div>
  </div>

  <h1 class="headline">ATTRACT MORE CUSTOMERS<br>MAKE MORE MONEY</h1>

  <ul class="benefits">
    <li><svg viewBox="0 0 20 18"><path d="M1,9 L7,15 L19,2" fill="none" stroke="var(--blue-bright)" stroke-width="3.5"/></svg>97% of people look online for businesses. You need a website</li>
    <li><svg viewBox="0 0 20 18"><path d="M1,9 L7,15 L19,2" fill="none" stroke="var(--blue-bright)" stroke-width="3.5"/></svg>You’re losing many customers by not having a website</li>
    <li><svg viewBox="0 0 20 18"><path d="M1,9 L7,15 L19,2" fill="none" stroke="var(--blue-bright)" stroke-width="3.5"/></svg>Beat your competition with better visibility and credibility</li>
    <li><svg viewBox="0 0 20 18"><path d="M1,9 L7,15 L19,2" fill="none" stroke="var(--blue-bright)" stroke-width="3.5"/></svg>Beautiful websites available now</li>
    <li><svg viewBox="0 0 20 18"><path d="M1,9 L7,15 L19,2" fill="none" stroke="var(--blue-bright)" stroke-width="3.5"/></svg>Smart, clean website designs ($3000 value. No extra charge)</li>
    <li><svg viewBox="0 0 20 18"><path d="M1,9 L7,15 L19,2" fill="none" stroke="var(--blue-bright)" stroke-width="3.5"/></svg>limited to only 4 websites per area.Don’t miss out!</li>
    <li><svg viewBox="0 0 20 18"><path d="M1,9 L7,15 L19,2" fill="none" stroke="var(--blue-bright)" stroke-width="3.5"/></svg>Social media setupoptions (searchly &amp; friendnet)</li>
  </ul>

  <div class="photo photo-touchscreen" role="img" aria-label="Businessman touching a floating touchscreen of web page thumbnails"></div>
  <div class="photo photo-boardroom" role="img" aria-label="Hand touching a digital interface in a modern boardroom"></div>

  <div class="url-pill">www.novaweb-example.com</div>

  <p class="pitch">Stop Wasting Money<br>On Mailers And Print<br>Advertising</p>

  <div class="globe" role="img" aria-label="Illustration of a blue globe surrounded by computer screens and devices"></div>

  <div class="price"><div class="price-inner">
    <div class="price-label">PRICING</div>
    <div class="price-amount">ONLY $99<br>/ MONTH</div>
    <div class="price-note">(That’s $3.30/Day)<br>(No other costs)</div>
  </div></div>

  <div class="footer-phone">1-800-555-0142</div>
</main>
</body>
</html>
```